No Credit Score QT and ZMR

I'm looking for a banner to display on emails as well as facebook. The facebook banner would need to be square and the other size is 728 x 90. We are a mortgage company that does mostly Military home loans. We would like to start out with just this banner, then do about 20 others once we find the right designer. I need something simple but that stands out. Our company website is www.harborpeakfinancial.com. The text for this will be ( Ask about our "No Credit Score" program for ZMR and QT)

```html
<!DOCTYPE html>
<html lang="en">
<head>
<meta charset="utf-8">
<title>Harbor Peak Financial – No Credit Score Banners</title>
<link href="https://fonts.googleapis.com/css2?family=Anton&display=swap" rel="stylesheet">
<style>
  :root {
    --green: #80a637;
    --green-dark: #4d7022;
    --ink: #111111;
    --white: #ffffff;
    --paper-light: #f7f7f8;
    --paper-mid: #e4e5e7;
    --art-tone: #d9dadd;
  }
  html, body {
    margin: 0;
    padding: 0;
    width: 1200px;
    height: 1200px;
    overflow: hidden;
    background: var(--white);
  }
  .canvas {
    position: relative;
    width: 1200px;
    height: 1200px;
  }
  .banner-square {
    position: absolute;
    left: 208px;
    top: 74px;
    width: 782px;
    height: 782px;
  }
  .banner-leaderboard {
    position: absolute;
    left: 64px;
    top: 941px;
    width: 1070px;
    height: 134px;
  }
  .type {
    font-family: "Anton", "Arial Narrow", sans-serif;
  }
  .brand-name { fill: var(--ink); }
  .callout { fill: var(--white); }
  .headline { fill: var(--ink); }
</style>
</head>
<body>
<main class="canvas">

  <!-- Square social banner -->
  <svg class="banner-square" viewBox="0 0 978 978" aria-label="Square banner: Ask about our No Credit Score program for ZMR and QT">
    <defs>
      <linearGradient id="paper" x1="0" y1="0" x2="1" y2="1">
        <stop offset="0" stop-color="var(--paper-light)"/>
        <stop offset="1" stop-color="var(--paper-mid)"/>
      </linearGradient>
      <radialGradient id="drop-shadow" cx="0.5" cy="0.5" r="0.5">
        <stop offset="0" stop-color="#b9babd" stop-opacity="0.8"/>
        <stop offset="1" stop-color="#b9babd" stop-opacity="0"/>
      </radialGradient>
    </defs>

    <rect class="backdrop" x="0" y="0" width="978" height="978" fill="url(#paper)"/>
    <ellipse class="ribbon-shadow" cx="700" cy="930" rx="190" ry="28" fill="url(#drop-shadow)"/>
    <polygon class="ribbon-fold" points="978,713 885,846 905,745" fill="var(--green-dark)"/>
    <polygon class="ribbon" points="0,273 978,48 978,713 0,938" fill="var(--green)"/>

    <g class="brand">
      <rect x="48" y="40" width="58" height="58" fill="var(--ink)"/>
      <text class="type brand-name" x="128" y="98" font-size="64" letter-spacing="6">HARBOR PEAK</text>
      <text class="type brand-name" x="132" y="124" font-size="17" letter-spacing="11">FINANCIAL, LLC</text>
    </g>

    <rect class="megaphone-art" x="95" y="263" width="445" height="325" rx="18"
          fill="var(--art-tone)" role="img" aria-label="Illustration of a megaphone announcing the offer"/>

    <g class="type callout" font-size="120" text-anchor="middle">
      <text x="690" y="262" transform="rotate(-7 690 212)">ASK</text>
      <text x="712" y="392" textLength="268" lengthAdjust="spacingAndGlyphs" transform="rotate(-7 712 342)">ABOUT</text>
      <text x="740" y="500" transform="rotate(-7 740 450)">OUR</text>
    </g>

    <g class="type headline">
      <text x="30" y="800" font-size="130" textLength="920" lengthAdjust="spacingAndGlyphs"
            transform="rotate(-12.5 30 800)">"No Credit Score"</text>
      <text x="105" y="865" font-size="72" textLength="845" lengthAdjust="spacingAndGlyphs"
            transform="rotate(-12.5 105 865)">Program for ZMR and QT</text>
    </g>

    <rect class="frame" x="1.5" y="1.5" width="975" height="975" fill="none" stroke="var(--green)" stroke-width="3"/>
  </svg>

  <!-- 728 x 90 email banner -->
  <svg class="banner-leaderboard" viewBox="0 0 1338 168" aria-label="Email banner: Ask about our No Credit Score program for ZMR and QT">
    <rect class="band" x="0" y="0" width="1338" height="168" fill="var(--green)"/>
    <polygon class="edge-left" points="0,0 0,168 35,168" fill="var(--green-dark)"/>
    <polygon class="brand-panel" points="0,0 385,0 420,168 35,168" fill="var(--white)"/>
    <polygon class="stripe" points="396,0 404,0 440,168 432,168" fill="var(--white)"/>
    <polygon class="stripe" points="1288,0 1298,0 1340,168 1330,168" fill="var(--white)"/>
    <polygon class="edge-right" points="1298,0 1338,0 1338,168 1340,168" fill="var(--green-dark)"/>

    <g class="brand">
      <rect x="38" y="58" width="40" height="40" fill="var(--ink)"/>
      <text class="type brand-name" x="92" y="96" font-size="42" letter-spacing="4">HARBOR PEAK</text>
      <text class="type brand-name" x="94" y="114" font-size="12" letter-spacing="8">FINANCIAL, LLC</text>
    </g>

    <rect class="megaphone-art" x="460" y="40" width="150" height="110" rx="8"
          fill="var(--art-tone)" role="img" aria-label="Illustration of a megaphone"/>

    <g class="type callout" font-size="50" text-anchor="middle">
      <text x="713" y="54">ASK</text>
      <text x="713" y="106">ABOUT</text>
      <text x="713" y="158">OUR</text>
    </g>

    <g class="type headline">
      <text x="825" y="102" font-size="70" textLength="443" lengthAdjust="spacingAndGlyphs">"No Credit Score"</text>
      <text x="845" y="140" font-size="40" textLength="405" lengthAdjust="spacingAndGlyphs">Program for ZMR and QT</text>
    </g>

    <rect class="frame" x="1.5" y="1.5" width="1335" height="165" fill="none" stroke="var(--green)" stroke-width="3"/>
  </svg>

</main>
</body>
</html>
```